Lodging Venture Advisors

I am an independent operator engaged on short/medium term consultancy briefs within the Hotel/Resort sector in the Pacific Area and have a representation in Fiji.

A broad based services is offered and includes:

Development Advisory
Property Management
Sales & Marketing
Holiday Ownership/Timeshare
Resorts/Apartments/Motels/Flashpackers/B&B
Financial & Legal Referrals

Industry/Entity Type

Hotel

Contact Information for Business Card

Business name - LODGING VENTURE ADVISORS
My name - Grant Whitlock
Address: PO Box 382 Coral Heights 4219 Qld
Phone: Australia: +61 7 55904283 Mobile: 0418952064 (Viber)
Fiji: +679 8527319
Email: grantmwhitlock@netmailbox.example

```html
<!DOCTYPE html>
<html lang="en">
<head>
<meta charset="utf-8">
<title>Lodging Venture Advisors — Business Card</title>
<link rel="stylesheet" href="https://fonts.googleapis.com/css2?family=Open+Sans:wght@400;700&display=swap">
<style>
  :root {
    --bg: #e9e6e1;
    --card-top: #ffffff;
    --card-bottom: #e4e4e4;
    --brand-red: #e2323f;
    --ink: #2a2a2a;
    --icon-blue: #3d4ba3;
    --white: #ffffff;
  }
  * { box-sizing: border-box; margin: 0; padding: 0; }
  html, body { width: 1200px; height: 894px; overflow: hidden; }
  body {
    background: var(--bg);
    font-family: "Open Sans", sans-serif;
    display: flex;
    flex-direction: column;
    align-items: center;
    justify-content: center;
    gap: 60px;
  }
  .card {
    position: relative;
    width: 600px;
    height: 343px;
    border-radius: 22px;
    overflow: hidden;
    background: linear-gradient(160deg, var(--card-top) 20%, var(--card-bottom) 100%);
    box-shadow: 0 10px 24px rgba(0,0,0,0.18);
  }
  .brand-name {
    font-family: "Open Sans", sans-serif;
    font-weight: 700;
    color: var(--brand-red);
    text-transform: uppercase;
    letter-spacing: 1px;
    line-height: 1.3;
  }
  .card-back .brand-name {
    position: absolute;
    left: 150px;
    top: 116px;
    font-size: 28px;
  }
  .card-front .brand-name {
    position: absolute;
    right: 40px;
    top: 36px;
    font-size: 22px;
    text-align: left;
  }
  .name-tab {
    position: absolute;
    left: 0;
    top: 118px;
    width: 300px;
    height: 64px;
    background: var(--brand-red);
    border-radius: 0 32px 32px 0;
    color: var(--white);
    padding: 10px 0 0 40px;
  }
  .person-name { font-size: 19px; font-weight: 700; letter-spacing: 1px; text-transform: uppercase; line-height: 1.1; }
  .person-role { font-size: 12px; letter-spacing: 0.5px; text-transform: uppercase; margin-top: 4px; }
  .contact-list {
    position: absolute;
    left: 40px;
    top: 196px;
    list-style: none;
    color: var(--ink);
    font-size: 13px;
    text-transform: uppercase;
  }
  .contact-list li { display: flex; align-items: center; gap: 10px; height: 20px; }
  .contact-list svg { width: 14px; height: 14px; flex: none; }
  .contact-list .address { align-items: flex-start; height: auto; line-height: 18px; }
  .contact-list .address svg { margin-top: 2px; }
  .accent-band {
    position: absolute;
    left: 0; right: 0; bottom: 0;
    height: 24px;
    background: var(--brand-red);
  }
</style>
</head>
<body>

  <section class="card card-back" aria-label="Card back">
    <h1 class="brand-name">Lodging<br>Venture<br>Advisors</h1>
  </section>

  <section class="card card-front" aria-label="Card front">
    <h2 class="brand-name">Lodging<br>Venture<br>Advisors</h2>

    <div class="name-tab">
      <p class="person-name">Grant Whitlock</p>
      <p class="person-role">Hotel Consultant</p>
    </div>

    <ul class="contact-list">
      <li>
        <svg viewBox="0 0 14 14" fill="none" stroke="var(--icon-blue)" stroke-width="1.2"><circle cx="7" cy="7" r="6.3"/><rect x="4.6" y="3.6" width="4.8" height="6.8" rx="0.8"/></svg>
        <span>+61 7 5550 4283</span>
      </li>
      <li>
        <svg viewBox="0 0 14 14" fill="none" stroke="var(--icon-blue)" stroke-width="1.2"><circle cx="7" cy="7" r="6.3"/><path d="M4.5 4 L6 4 L6.6 5.8 L5.8 6.5 Q6.6 8 7.6 8.4 L8.3 7.6 L10 8.2 L10 9.6 Q6 10 4.4 5.6 Z" fill="var(--icon-blue)" stroke="none"/></svg>
        <span>0491 570 158</span>
      </li>
      <li>
        <svg viewBox="0 0 14 14" fill="none" stroke="var(--icon-blue)" stroke-width="1.2"><circle cx="7" cy="7" r="6.3"/><rect x="3.8" y="4.8" width="6.4" height="4.6"/><path d="M3.8 4.8 L7 7.4 L10.2 4.8"/></svg>
        <span>grantmwhitlock@netmailbox.example</span>
      </li>
      <li>
        <svg viewBox="0 0 14 14" fill="none" stroke="var(--icon-blue)" stroke-width="1.1"><circle cx="7" cy="7" r="6.3"/><circle cx="7" cy="7" r="3.4"/><path d="M3.6 7 H10.4 M7 3.6 Q5.3 7 7 10.4 M7 3.6 Q8.7 7 7 10.4"/></svg>
        <span>www.lodgingventure.example</span>
      </li>
      <li class="address">
        <svg viewBox="0 0 14 14" fill="none" stroke="var(--icon-blue)" stroke-width="1.2"><circle cx="7" cy="7" r="6.3"/><path d="M7 10.6 Q4.4 7.6 4.4 6 A2.6 2.6 0 0 1 9.6 6 Q9.6 7.6 7 10.6 Z" fill="var(--icon-blue)" stroke="none"/></svg>
        <span>PO Box 382 Coral Heights<br>4219 Qld</span>
      </li>
    </ul>

    <div class="accent-band"></div>
  </section>

</body>
</html>
```